Please design a business card with my current logo (attached below).

I have some specifics that must be included:
1. I want the emphasis on Accredited Legacy Home Transfer Advisor.
2. Leave room for my picture.
3. Company name, address, phone numbers and email address.
4. My BRE# should be placed under my name.

```html
<!DOCTYPE html>
<html lang="en">
<head>
<meta charset="utf-8">
<title>Maren Holt – Business Card</title>
<link rel="stylesheet" href="https://fonts.googleapis.com/css2?family=Cinzel:wght@500&family=Open+Sans:wght@400;600;700;800&display=swap">
<style>
  :root {
    --bg: #e6e3df;
    --card-dark: #2b2a2c;
    --card-dark-light: #3d3c3f;
    --brand-red: #c8193f;
    --white: #ffffff;
    --soft-white: #e8e8e8;
    --strip: #f4f4f4;
    --photo-a: #d9d6d3;
    --photo-b: #8a7468;
  }
  * { box-sizing: border-box; margin: 0; padding: 0; }
  html, body { width: 1200px; height: 1000px; overflow: hidden; }
  body {
    background: var(--bg);
    font-family: "Open Sans", Arial, sans-serif;
    position: relative;
  }
  .card {
    position: absolute;
    left: 250px;
    width: 700px;
    height: 400px;
    background: radial-gradient(ellipse at 40% 30%, var(--card-dark-light), var(--card-dark) 70%);
    box-shadow: 0 10px 30px rgba(0,0,0,.25);
    overflow: hidden;
  }
  .card--front { top: 60px; }
  .card--back  { top: 540px; display: flex; align-items: center; justify-content: center; }

  .portrait-frame {
    position: absolute;
    left: 470px; top: 28px;
    width: 190px; height: 200px;
    background: var(--white);
    padding: 8px;
  }
  .portrait {
    width: 100%; height: 100%;
    background: linear-gradient(160deg, var(--photo-a), var(--photo-b));
  }

  .identity { position: absolute; left: 50px; top: 62px; }
  .brand-name {
    display: flex; align-items: center; gap: 14px;
    font-family: "Cinzel", Georgia, serif;
    font-weight: 500;
    color: var(--white);
    font-size: 44px;
    line-height: 1.2;
    letter-spacing: 1px;
  }
  .brand-mark { width: 26px; height: 26px; background: var(--brand-red); flex: none; }
  .license {
    margin-top: 4px;
    margin-left: 40px;
    color: var(--white);
    font-weight: 600;
    font-size: 15px;
    letter-spacing: .8px;
  }
  .address {
    margin-top: 12px;
    margin-left: 40px;
    color: var(--soft-white);
    font-size: 17px;
    line-height: 1.45;
  }

  .title-strip {
    position: absolute; left: 0; top: 260px;
    width: 100%; height: 46px;
    background: var(--strip);
    color: var(--brand-red);
    font-weight: 800;
    font-size: 21px;
    text-transform: uppercase;
    letter-spacing: .5px;
    display: flex; align-items: center;
    padding-left: 40px;
    white-space: nowrap;
  }
  .contact-band {
    position: absolute; left: 0; top: 306px;
    width: 100%; height: 94px;
    background: var(--brand-red);
    padding: 8px 40px;
    list-style: none;
  }
  .contact-band li {
    display: flex; align-items: center; gap: 12px;
    color: var(--white);
    font-weight: 700;
    font-size: 17px;
    height: 26px;
  }
  .contact-band svg { width: 20px; height: 20px; flex: none; }

  .card--back .brand-name { font-size: 62px; gap: 20px; }
  .card--back .brand-mark { width: 36px; height: 36px; }
</style>
</head>
<body>

<section class="card card--front" aria-label="Card front">
  <div class="portrait-frame">
    <div class="portrait" role="img" aria-label="Portrait photo of the agent"></div>
  </div>

  <div class="identity">
    <div class="brand-name"><span class="brand-mark"></span>Maren Holt</div>
    <p class="license">BRE# 01987654</p>
    <p class="address">42 Alder Street, Suite B<br>Oakdale, CA 95361</p>
  </div>

  <div class="title-strip">Accredited Legacy Home Transfer Advisor</div>

  <ul class="contact-band">
    <li>
      <svg viewBox="0 0 20 20" fill="none" stroke="#fff" stroke-width="2"><rect x="5" y="1.5" width="10" height="17" rx="2"/><line x1="9" y1="15" x2="11" y2="15"/></svg>
      (555) 204-1187
    </li>
    <li>
      <svg viewBox="0 0 20 20" fill="none" stroke="#fff" stroke-width="2"><rect x="1.5" y="4" width="17" height="12"/><polyline points="1.5,4 10,11 18.5,4"/></svg>
      marenholt@example.com
    </li>
    <li>
      <svg viewBox="0 0 20 20" fill="none" stroke="#fff" stroke-width="2"><polyline points="2,10 10,3 18,10"/><polyline points="4.5,8 4.5,17 15.5,17 15.5,8"/></svg>
      Ridgeway Realty
    </li>
  </ul>
</section>

<section class="card card--back" aria-label="Card back">
  <div class="brand-name"><span class="brand-mark"></span>Maren Holt</div>
</section>

</body>
</html>
```